Landing Page for Bathroom Remodeling Webpage - Desktop and Mobile

I am looking for some help designing the "above the fold" area for my bathroom remodeling service page. Looking for something a little different than the rest. Typically remodeling companies just put a nice picture of a bathroom remodel but I would like to do something a little different / more creative. Below is a link to the current wireframe we are working on.
Current website is located at plumvantaridge.com
Again the biggest thing I am looking for is a design for the very top section but would love help on the rest of the page as well. You will see by viewing the link below the type of information we are looking to include on the page:
PLEASE DO INCLUDE WHAT THE MOBILE VERSION WOULD LOOK LIKE AS WELL.
Wireframe:
https://boards.quillmerra.com/view/3f8a1b2c-90de-4e7a-b5c1-aa62d09e1f35-418k/
There are also comments in the link above you can read as well.
We like the idea of something interactive such as this...
https://pixorvale.com/shots/5192746-Glenhart-Scooter-Store-Animation
Attached is also the logo we want to use going forward
Target Market(s)
Residential homeowners, 30 years old+ with professional careers
Number of Pages Required
1 page
Look and feel
Each slider illustrates characteristics of the customer's brand and the style your logo design should communicate.

```html
<!DOCTYPE html>
<html lang="en">
<head>
<meta charset="utf-8">
<title>Plumvanta – Bathroom Remodeling</title>
<link href="https://fonts.googleapis.com/css2?family=Poppins:wght@300;400;500;600;700&display=swap" rel="stylesheet">
<style>
:root{
  --navy:#0d2a52;
  --red:#d40f14;
  --ink:#1f2a3c;
  --muted:#555d6b;
  --pale:#e7effa;
  --footer:#e3eaf4;
  --line:#c9cfd8;
  --link:#e0453e;
  --white:#fff;
}
*{box-sizing:border-box;margin:0;padding:0}
html,body{width:1200px;height:4706px;overflow:hidden;background:var(--white);font-family:"Poppins",sans-serif;color:var(--ink)}
.page{position:relative;width:1200px;height:4706px;overflow:hidden}
.abs{position:absolute}
.center{text-align:center;left:0;width:1200px}
.section-title{position:absolute;left:0;width:1200px;text-align:center;font-weight:400;font-size:34px;color:var(--navy);letter-spacing:.3px}
.section-title.on-navy{color:var(--white)}
.subtitle{position:absolute;left:0;width:1200px;text-align:center;font-size:9.5px;color:var(--muted)}

/* header */
.header{position:absolute;left:0;top:0;width:1200px;height:72px}
.brand{position:absolute;display:flex;align-items:center;gap:7px;font-weight:700;font-size:22px;color:var(--red);letter-spacing:.3px}
.brand .mark{width:18px;height:18px;background:var(--navy);border-radius:50%}
.nav{position:absolute;left:378px;top:40px;display:flex;gap:29px;font-size:11px;color:var(--ink)}
.contact-mini{position:absolute;left:852px;top:24px;font-size:9px;color:var(--red);line-height:1.4}
.contact-mini span{color:var(--ink);display:flex;align-items:center;gap:4px}
.btn-nav{position:absolute;left:977px;top:18px;width:123px;height:38px;background:var(--navy);color:#fff;font-size:11px;font-weight:500;display:flex;align-items:center;justify-content:center}

.navy-band{position:absolute;left:0;width:1200px;background:var(--navy)}
.photo{position:absolute}
.hero-photo{left:100px;top:72px;width:1000px;height:500px;background:
  linear-gradient(90deg,rgba(90,90,88,.55) 0%,rgba(90,90,88,.45) 22%,rgba(255,255,255,0) 23%,rgba(255,255,255,0) 64%,rgba(95,95,92,.5) 65%,rgba(95,95,92,.5) 76%,rgba(255,255,255,0) 77%),
  linear-gradient(180deg,#f3f2f0 0%,#ebeae7 55%,#d9d8d5 100%)}
.project{top:778px;width:317px;height:320px}
.project .label{position:absolute;left:15px;bottom:28px;color:#fff;font-size:14px;font-weight:300}
.more{position:absolute;left:0;width:1200px;text-align:center;font-size:9px;color:var(--red)}
.more .plus{display:block;margin:0 auto 4px;width:30px;height:30px}

.intro-text{position:absolute;left:270px;width:660px;text-align:center;font-size:9.5px;line-height:18.5px;color:var(--muted)}

.btn-red{position:absolute;background:var(--red);color:#fff;display:flex;align-items:center;justify-content:center;font-weight:400}

/* materials */
.mat-box{position:absolute;top:1902px;width:156px;height:98px;background:var(--pale);border:1px solid #b8c8de}
.mat-box svg{position:absolute;left:8px;top:12px}
.mat-box b{position:absolute;left:8px;top:50px;font-size:11.5px;color:var(--navy);font-weight:600;line-height:1.05}
.mat-list{position:absolute;top:2008px;width:156px;list-style:none;font-size:8.5px;color:var(--ink);line-height:1.05}
.mat-list li{display:flex;gap:4px;margin-bottom:8px}
.tick{flex:none;width:9px;height:9px}

/* pricing */
.pricing{position:absolute;left:271px;top:2345px;width:658px;height:310px;display:flex}
.plan{flex:1;padding:20px 26px 0;text-align:center}
.plan.a{background:linear-gradient(90deg,#e6ebf1,#c8d0da)}
.plan.b{background:#e4ecf7}
.plan.c{background:linear-gradient(90deg,#c8d0da,#dde3ea)}
.plan h3{font-size:17px;font-weight:600;color:var(--navy)}
.plan p{font-size:8.5px;color:var(--muted);line-height:1.3;margin-top:6px}
.plan .price{font-size:28px;color:var(--navy);margin-top:2px;border-bottom:1px solid #8d99aa;padding-bottom:4px}
.plan ul{list-style:none;text-align:left;font-size:8.5px;margin-top:12px;line-height:15.6px}
.plan li{display:flex;gap:6px;align-items:center}

/* appointment */
.steps{position:absolute;left:100px;top:2863px;width:541px;height:31px;display:flex;border:1.5px solid var(--navy);font-size:11px}
.steps div{flex:1;display:flex;align-items:center;justify-content:center;color:var(--ink)}
.steps .on{background:var(--red);color:#fff}
.opt{position:absolute;left:120px;width:505px;border:1.5px solid var(--line);padding:12px 16px;font-size:8.5px;line-height:17px;color:var(--ink)}
.opt b{font-weight:500;display:block}
.step-info{position:absolute;left:687px;width:413px}
.step-info h4{font-size:22px;font-weight:400;color:var(--navy)}
.step-info p{font-size:8.8px;line-height:17px;color:var(--muted);margin-top:8px}

/* articles */
.article{position:absolute;top:3404px;width:312px;height:291px;background:#ebe9e8;border:1.5px solid #cfcfcf}
.article .photo{left:0;top:0;width:309px;height:165px;position:absolute}
.article .date{position:absolute;left:28px;top:188px;font-size:14px;color:var(--ink)}
.article .title{position:absolute;left:28px;top:215px;width:240px;font-size:8.8px;line-height:12px;color:var(--muted)}

.faq{position:absolute;left:443px;top:3970px;width:313px;border:1.5px solid var(--line)}
.faq div{height:30.5px;display:flex;align-items:center;justify-content:space-between;padding:0 12px;font-size:8.8px;border-bottom:1.5px solid var(--line)}
.faq div:last-child{border-bottom:none}
.faq span.p{font-size:13px}

/* footer */
.footer{position:absolute;left:0;top:4290px;width:1200px;height:350px;background:var(--footer)}
.foot-col{position:absolute}
.foot-col h5{font-size:14px;font-weight:600;color:var(--red)}
.foot-col ul{list-style:none;font-size:14px;color:var(--link);line-height:31px;margin-top:4px;font-weight:400}
.social{position:absolute;left:183px;top:4378px;display:flex;gap:3px}
.social span{width:27px;height:27px;display:block}
.bottom{position:absolute;left:0;top:4640px;width:1200px;height:66px;background:var(--footer);border-top:1px solid #c3cbd6}
</style>
</head>
<body>
<div class="page">

  <header class="header">
    <div class="brand" style="left:100px;top:24px"><span class="mark"></span>PLUMVANTA</div>
    <nav class="nav"><span>Home</span><span>Services</span><span>Videos</span><span>Gallery</span><span>Blog</span><span>About</span><span>Contact</span></nav>
    <div class="contact-mini">Have any Questions?
      <span><svg width="9" height="9" viewBox="0 0 24 24"><path fill="#1f2a3c" d="M6.6 10.8a15 15 0 0 0 6.6 6.6l2.2-2.2c.3-.3.7-.4 1-.2 1.1.4 2.3.6 3.6.6.6 0 1 .4 1 1V20c0 .6-.4 1-1 1A17 17 0 0 1 3 4c0-.6.4-1 1-1h3.5c.6 0 1 .4 1 1 0 1.3.2 2.5.6 3.6.1.3 0 .7-.2 1z"/></svg>555-204-7318</span></div>
    <div class="btn-nav">Get Schedule</div>
  </header>

  <!-- hero -->
  <div class="navy-band" style="top:292px;height:673px"></div>
  <div class="photo hero-photo" role="img" aria-label="Bright modern bathroom with grey stone walls, white bathtub, glass shower and floating vanity"></div>
  <h2 class="section-title on-navy" style="top:646px">Get inspired by similar projects</h2>
  <div class="photo project" style="left:100px;background:linear-gradient(160deg,#c6c4c0,#e8e6e2 60%,#a9a7a2)" role="img" aria-label="Marble bathroom vanity with vessel sink and plants"><span class="label">Project title</span></div>
  <div class="photo project" style="left:442px;background:linear-gradient(170deg,#cdb99a,#e9dcc6 55%,#b59a74)" role="img" aria-label="Beige travertine bathroom with arched doorway"><span class="label">Project title</span></div>
  <div class="photo project" style="left:783px;background:linear-gradient(160deg,#d4d4d6,#efeff0 55%,#b3b3b6)" role="img" aria-label="Grey marble bathroom with freestanding tub"><span class="label">Project title</span></div>
  <div class="more" style="top:1112px"><svg class="plus" viewBox="0 0 30 30"><circle cx="15" cy="15" r="13" fill="none" stroke="#d40f14" stroke-width="1.5"/><path d="M15 9v12M9 15h12" stroke="#d40f14" stroke-width="1.5"/></svg>Show me more</div>

  <!-- intro -->
  <h2 class="section-title" style="top:1236px">Bathroom Remodeling Made Simple</h2>
  <p class="intro-text" style="top:1302px">Lorem ipsum dolor sit amet, consectetur adipiscing elit, sed do eiusmod tempor incididunt ut labore et dolore magna aliqua. Quis ipsum suspendisse ultrices gravida. Risus commodo viverra maecenas accumsan lacus vel facilisis. Lorem ipsum dolor sit amet, consectetur adipiscing elit, sed do eiusmod tempor incididunt ut labore et dolore magna aliqua. Quis ipsum suspendisse ultrices gravida. Risus commodo viverra maecenas accumsan lacus vel facilisis. Lorem ipsum dolor sit amet, consectetur adipiscing elit, sed do eiusmod tempor incididunt ut labore et dolore magna aliqua. Quis ipsum suspendisse ultrices gravida.</p>
  <div class="more" style="top:1430px"><svg class="plus" viewBox="0 0 30 30"><circle cx="15" cy="15" r="13" fill="none" stroke="#d40f14" stroke-width="1.5"/><path d="M15 9v12M9 15h12" stroke="#d40f14" stroke-width="1.5"/></svg>Show me more</div>

  <!-- CTA 1 -->
  <div class="navy-band" style="top:1550px;height:128px"></div>
  <p class="abs" style="left:152px;top:1604px;font-size:14px;color:#fff">Schedule a free in home consulation via our online appointment scheduling system</p>
  <div class="btn-red" style="left:846px;top:1582px;width:200px;height:64px;font-size:22px">Schedule</div>

  <!-- materials -->
  <svg class="abs" style="left:577px;top:1728px" width="46" height="36" viewBox="0 0 46 36"><g fill="#0d2a52"><rect x="0" y="0" width="8" height="7"/><rect x="11" y="0" width="35" height="7"/><rect x="0" y="10" width="8" height="7"/><rect x="11" y="10" width="35" height="7"/><rect x="0" y="20" width="8" height="7"/><rect x="11" y="20" width="35" height="7"/><rect x="0" y="30" width="8" height="6"/><rect x="11" y="30" width="35" height="6"/></g></svg>
  <h2 class="section-title" style="top:1798px">Material Selections</h2>
  <p class="subtitle" style="top:1856px">Four your bathroom remodel there will be material selections you will have to make. Use the lists below to get an idea of some of the options</p>

  <div class="mat-box" style="left:100px"><svg width="32" height="32" viewBox="0 0 32 32"><circle cx="16" cy="16" r="13" fill="none" stroke="#0d2a52" stroke-width="2.5"/><path d="M18 6l-8 11h6l-2 9 8-11h-6z" fill="#0d2a52"/></svg><b>Electrical</b></div>
  <div class="mat-box" style="left:268px"><svg width="34" height="32" viewBox="0 0 34 32"><path d="M4 4h6v4H6v6h26v4a8 8 0 0 1-8 8H10a8 8 0 0 1-8-8v-4h2z" fill="#0d2a52"/></svg><b>Plumbing</b></div>
  <div class="mat-box" style="left:438px"><svg width="80" height="32" viewBox="0 0 80 32"><path d="M2 14L30 4l48 8-28 12z" fill="#0d2a52"/><path d="M16 9l46 9M40 6L30 20" stroke="#e7effa" stroke-width="2"/></svg><b>Tile &amp; Flooring</b></div>
  <div class="mat-box" style="left:608px"><svg width="34" height="32" viewBox="0 0 34 32"><path d="M17 2L2 16h5v13h8v-8h4v8h8V16h5z" fill="#0d2a52"/></svg><b>Exterior Maintenance</b></div>
  <div class="mat-box" style="left:778px"><svg width="34" height="32" viewBox="0 0 34 32"><rect x="3" y="3" width="28" height="26" fill="none" stroke="#0d2a52" stroke-width="2.5"/><path d="M12 3v26M22 3v26" stroke="#0d2a52" stroke-width="2"/></svg><b>Doors &amp; Windows</b></div>
  <div class="mat-box" style="left:948px"><svg width="32" height="32" viewBox="0 0 32 32"><rect x="3" y="3" width="22" height="8" fill="none" stroke="#0d2a52" stroke-width="2.5"/><path d="M25 7h4v8H15v5" fill="none" stroke="#0d2a52" stroke-width="2.5"/><rect x="12" y="20" width="6" height="10" fill="#0d2a52"/></svg><b>Painting &amp; Drywall Repair</b></div>

  <ul class="mat-list" style="left:106px"><li><svg class="tick" viewBox="0 0 10 10"><path d="M1 5l3 3 5-7" fill="none" stroke="#1f2a3c" stroke-width="2"/></svg>Change outlets / switches</li><li><svg class="tick" viewBox="0 0 10 10"><path d="M1 5l3 3 5-7" fill="none" stroke="#1f2a3c" stroke-width="2"/></svg>Install under cabinet lighting</li><li><svg class="tick" viewBox="0 0 10 10"><path d="M1 5l3 3 5-7" fill="none" stroke="#1f2a3c" stroke-width="2"/></svg>Hang and replace lighting fixtures</li><li><svg class="tick" viewBox="0 0 10 10"><path d="M1 5l3 3 5-7" fill="none" stroke="#1f2a3c" stroke-width="2"/></svg>Install under cabinet lighting</li></ul>
  <ul class="mat-list" style="left:274px"><li><svg class="tick" viewBox="0 0 10 10"><path d="M1 5l3 3 5-7" fill="none" stroke="#1f2a3c" stroke-width="2"/></svg>Change out shower fixtures</li><li><svg class="tick" viewBox="0 0 10 10"><path d="M1 5l3 3 5-7" fill="none" stroke="#1f2a3c" stroke-width="2"/></svg>Change out vanity fixtures</li><li><svg class="tick" viewBox="0 0 10 10"><path d="M1 5l3 3 5-7" fill="none" stroke="#1f2a3c" stroke-width="2"/></svg>Replace toilet</li></ul>
  <ul class="mat-list" style="left:444px"><li><svg class="tick" viewBox="0 0 10 10"><path d="M1 5l3 3 5-7" fill="none" stroke="#1f2a3c" stroke-width="2"/></svg>Shower Wall Tile</li><li><svg class="tick" viewBox="0 0 10 10"><path d="M1 5l3 3 5-7" fill="none" stroke="#1f2a3c" stroke-width="2"/></svg>Shower Floor Tile</li><li><svg class="tick" viewBox="0 0 10 10"><path d="M1 5l3 3 5-7" fill="none" stroke="#1f2a3c" stroke-width="2"/></svg>Bathroom Flooring</li></ul>
  <ul class="mat-list" style="left:614px"><li><svg class="tick" viewBox="0 0 10 10"><path d="M1 5l3 3 5-7" fill="none" stroke="#1f2a3c" stroke-width="2"/></svg>Repair siding</li><li><svg class="tick" viewBox="0 0 10 10"><path d="M1 5l3 3 5-7" fill="none" stroke="#1f2a3c" stroke-width="2"/></svg>Repair deck</li><li><svg class="tick" viewBox="0 0 10 10"><path d="M1 5l3 3 5-7" fill="none" stroke="#1f2a3c" stroke-width="2"/></svg>Caulking</li><li><svg class="tick" viewBox="0 0 10 10"><path d="M1 5l3 3 5-7" fill="none" stroke="#1f2a3c" stroke-width="2"/></svg>Clean gutters</li></ul>
  <ul class="mat-list" style="left:784px"><li><svg class="tick" viewBox="0 0 10 10"><path d="M1 5l3 3 5-7" fill="none" stroke="#1f2a3c" stroke-width="2"/></svg>Adjust doors</li><li><svg class="tick" viewBox="0 0 10 10"><path d="M1 5l3 3 5-7" fill="none" stroke="#1f2a3c" stroke-width="2"/></svg>Replace doors</li><li><svg class="tick" viewBox="0 0 10 10"><path d="M1 5l3 3 5-7" fill="none" stroke="#1f2a3c" stroke-width="2"/></svg>Replace windows</li><li><svg class="tick" viewBox="0 0 10 10"><path d="M1 5l3 3 5-7" fill="none" stroke="#1f2a3c" stroke-width="2"/></svg>Replace trim</li></ul>
  <ul class="mat-list" style="left:954px"><li><svg class="tick" viewBox="0 0 10 10"><path d="M1 5l3 3 5-7" fill="none" stroke="#1f2a3c" stroke-width="2"/></svg>Painting and touchups</li><li><svg class="tick" viewBox="0 0 10 10"><path d="M1 5l3 3 5-7" fill="none" stroke="#1f2a3c" stroke-width="2"/></svg>Drywall Patching</li><li><svg class="tick" viewBox="0 0 10 10"><path d="M1 5l3 3 5-7" fill="none" stroke="#1f2a3c" stroke-width="2"/></svg>Drywall Texturing</li></ul>

  <!-- pricing -->
  <svg class="abs" style="left:579px;top:2160px" width="42" height="42" viewBox="0 0 42 42"><circle cx="21" cy="21" r="18" fill="none" stroke="#0d2a52" stroke-width="2.5" stroke-dasharray="5 3"/><circle cx="21" cy="21" r="12" fill="#0d2a52"/><text x="21" y="27" text-anchor="middle" font-family="Poppins,sans-serif" font-size="16" font-weight="700" fill="#fff">$</text></svg>
  <h2 class="section-title" style="top:2230px">Pricing Packages</h2>
  <p class="subtitle" style="top:2288px">Lorem ipsum dolor sit amet, consectetur adipiscing elit, sed do eiusmod tempor incididunt ut labore et dolore magna aliqua. minim veniam,</p>

  <div class="pricing">
    <div class="plan a"><h3>Minor Finish</h3><p>Gets the basement to the point of livable space</p><div class="price">$</div>
      <ul><li><svg class="tick" viewBox="0 0 10 10"><path d="M1 5l3 3 5-7" fill="none" stroke="#1f2a3c" stroke-width="2"/></svg>Framing</li><li><svg class="tick" viewBox="0 0 10 10"><path d="M1 5l3 3 5-7" fill="none" stroke="#1f2a3c" stroke-width="2"/></svg>Electrical Rought Ins</li><li><svg class="tick" viewBox="0 0 10 10"><path d="M1 5l3 3 5-7" fill="none" stroke="#1f2a3c" stroke-width="2"/></svg>Drywall</li><li><svg class="tick" viewBox="0 0 10 10"><path d="M1 5l3 3 5-7" fill="none" stroke="#1f2a3c" stroke-width="2"/></svg>Paint</li><li><svg class="tick" viewBox="0 0 10 10"><path d="M1 5l3 3 5-7" fill="none" stroke="#1f2a3c" stroke-width="2"/></svg>Trim &amp; Door</li><li><svg class="tick" viewBox="0 0 10 10"><path d="M1 5l3 3 5-7" fill="none" stroke="#1f2a3c" stroke-width="2"/></svg>Flooring</li><li><svg class="tick" viewBox="0 0 10 10"><path d="M1 5l3 3 5-7" fill="none" stroke="#1f2a3c" stroke-width="2"/></svg>Plumging Rough Ins</li><li><svg class="tick" viewBox="0 0 10 10"><path d="M1 5l3 3 5-7" fill="none" stroke="#1f2a3c" stroke-width="2"/></svg>Bathroom Addition</li><li><svg class="tick" viewBox="0 0 10 10"><path d="M1 5l3 3 5-7" fill="none" stroke="#1f2a3c" stroke-width="2"/></svg>Kitchen / Bar Addition</li><li><svg class="tick" viewBox="0 0 10 10"><path d="M1 5l3 3 5-7" fill="none" stroke="#1f2a3c" stroke-width="2"/></svg>Theater Room</li></ul></div>
    <div class="plan b"><h3>Moderate Finish</h3><p>type basement finish. Living space and bedrooms with a bathroom.</p><div class="price">$$</div>
      <ul><li><svg class="tick" viewBox="0 0 10 10"><path d="M1 5l3 3 5-7" fill="none" stroke="#1f2a3c" stroke-width="2"/></svg>Framing</li><li><svg class="tick" viewBox="0 0 10 10"><path d="M1 5l3 3 5-7" fill="none" stroke="#1f2a3c" stroke-width="2"/></svg>Electrical Rought Ins</li><li><svg class="tick" viewBox="0 0 10 10"><path d="M1 5l3 3 5-7" fill="none" stroke="#1f2a3c" stroke-width="2"/></svg>Drywall</li><li><svg class="tick" viewBox="0 0 10 10"><path d="M1 5l3 3 5-7" fill="none" stroke="#1f2a3c" stroke-width="2"/></svg>Paint</li><li><svg class="tick" viewBox="0 0 10 10"><path d="M1 5l3 3 5-7" fill="none" stroke="#1f2a3c" stroke-width="2"/></svg>Trim &amp; Door</li><li><svg class="tick" viewBox="0 0 10 10"><path d="M1 5l3 3 5-7" fill="none" stroke="#1f2a3c" stroke-width="2"/></svg>Flooring</li><li><svg class="tick" viewBox="0 0 10 10"><path d="M1 5l3 3 5-7" fill="none" stroke="#1f2a3c" stroke-width="2"/></svg>Plumging Rough Ins</li><li><svg class="tick" viewBox="0 0 10 10"><path d="M1 5l3 3 5-7" fill="none" stroke="#1f2a3c" stroke-width="2"/></svg>Bathroom Addition</li><li><svg class="tick" viewBox="0 0 10 10"><path d="M1 5l3 3 5-7" fill="none" stroke="#1f2a3c" stroke-width="2"/></svg>Kitchen / Bar Addition</li><li><svg class="tick" viewBox="0 0 10 10"><path d="M1 5l3 3 5-7" fill="none" stroke="#1f2a3c" stroke-width="2"/></svg>Theater Room</li></ul></div>
    <div class="plan c"><h3>Major Finish</h3><p>Moderate finish plus a kitchen, bathroom and potentially theater</p><div class="price">$</div>
      <ul><li><svg class="tick" viewBox="0 0 10 10"><path d="M1 5l3 3 5-7" fill="none" stroke="#1f2a3c" stroke-width="2"/></svg>Framing</li><li><svg class="tick" viewBox="0 0 10 10"><path d="M1 5l3 3 5-7" fill="none" stroke="#1f2a3c" stroke-width="2"/></svg>Electrical Rought Ins</li><li><svg class="tick" viewBox="0 0 10 10"><path d="M1 5l3 3 5-7" fill="none" stroke="#1f2a3c" stroke-width="2"/></svg>Drywall</li><li><svg class="tick" viewBox="0 0 10 10"><path d="M1 5l3 3 5-7" fill="none" stroke="#1f2a3c" stroke-width="2"/></svg>Paint</li><li><svg class="tick" viewBox="0 0 10 10"><path d="M1 5l3 3 5-7" fill="none" stroke="#1f2a3c" stroke-width="2"/></svg>Trim &amp; Door</li><li><svg class="tick" viewBox="0 0 10 10"><path d="M1 5l3 3 5-7" fill="none" stroke="#1f2a3c" stroke-width="2"/></svg>Flooring</li><li><svg class="tick" viewBox="0 0 10 10"><path d="M1 5l3 3 5-7" fill="none" stroke="#1f2a3c" stroke-width="2"/></svg>Plumging Rough Ins</li><li><svg class="tick" viewBox="0 0 10 10"><path d="M1 5l3 3 5-7" fill="none" stroke="#1f2a3c" stroke-width="2"/></svg>Bathroom Addition</li><li><svg class="tick" viewBox="0 0 10 10"><path d="M1 5l3 3 5-7" fill="none" stroke="#1f2a3c" stroke-width="2"/></svg>Kitchen / Bar Addition</li><li><svg class="tick" viewBox="0 0 10 10"><path d="M1 5l3 3 5-7" fill="none" stroke="#1f2a3c" stroke-width="2"/></svg>Theater Room</li></ul></div>
  </div>

  <!-- CTA 2 -->
  <div class="navy-band" style="top:2698px;height:128px"></div>
  <p class="abs" style="left:296px;top:2752px;font-size:14px;color:#fff">Schedule Your Free Consultation Today!</p>
  <div class="btn-red" style="left:652px;top:2728px;width:270px;height:64px;font-size:22px;gap:8px;border:1.5px solid #fff">
    <svg width="40" height="40" viewBox="0 0 40 40"><circle cx="20" cy="20" r="19" fill="#fff"/><circle cx="20" cy="20" r="15" fill="#d40f14"/><path d="M20 10v16M13 20l7 7 7-7" fill="none" stroke="#fff" stroke-width="3.5"/></svg>Schedule Below</div>

  <!-- appointment -->
  <div class="steps"><div class="on">Choose Appoinment</div><div>Your Info</div><div>Confirmation</div></div>
  <svg class="abs" style="left:290px;top:2863px" width="24" height="31" viewBox="0 0 24 31"><path d="M0 0l18 15.5L0 31" fill="#d40f14"/><path d="M4 0l18 15.5L4 31" fill="none" stroke="#0d2a52" stroke-width="1.5"/></svg>
  <svg class="abs" style="left:482px;top:2863px" width="22" height="31" viewBox="0 0 22 31"><path d="M2 0l18 15.5L2 31" fill="none" stroke="#0d2a52" stroke-width="1.5"/></svg>
  <p class="abs" style="left:122px;top:2928px;width:480px;font-size:8.5px;line-height:17px;color:var(--ink)">Find a time that works best for your schedule. If you cannot find a time that works for you please contact us. We will be flexible on finding a time that works best for you.</p>
  <div class="opt" style="top:2989px;height:94px"><b>Estimate</b>If you are ready for us to visit you at your home this option is for you. Our experts will meet you at your house to discuss the project. Within a few days you will have our proposal in your hands.</div>
  <div class="opt" style="top:3091px;height:74px"><b>Conference Call</b>Just want to chat about a potential project? Schedule a time and one of our experts will call to discuss your project.</div>
  <div class="opt" style="top:3173px;height:92px"><b>Virtual Appointment (Meetly Meeting)</b>NEW OPTION: Due to the coronavirus we are beginning to offer virtual appointments. We will do this via Callwave or Meetly meetings so we can see your space and give you a rough estimate for the project. Once everything passes over we will then be ready to hit the ground running sooner.</div>

  <div class="step-info" style="top:2858px"><h4>1. Schedule an Appointment Today</h4><p>View our calendar on the left and pick an appointment time that works best for you. Even though we show our handyman out at an hourly rate we like to see the project prior to sending our handyman over. This will allow us to properly prepare for your project and save you money.</p></div>
  <div class="step-info" style="top:3009px"><h4>2. Appointment</h4><p>View our calendar on the left and pick an appointment time that works best for you. Even though we show our handyman out at an hourly rate we like to see the project prior to sending our handyman over. This will allow us to properly prepare for your project and save you money.</p></div>
  <div class="step-info" style="top:3166px"><h4>3. Schedule Job</h4><p>If the estimate is acceptable we will proceed with scheduling the job at a time that works well for you.</p></div>

  <!-- articles -->
  <h2 class="section-title" style="top:3318px">Helpful Articles</h2>
  <div class="article" style="left:120px"><div class="photo" style="background:linear-gradient(150deg,#8c8f86,#dcdcd8 55%,#6f7268)" role="img" aria-label="Bathroom with green tile shower and vanity"></div><span class="date">Dana 02.03.2021</span><span class="title">7 Key Things to Consider Before Remodeling the Kitchen</span></div>
  <div class="article" style="left:446px"><div class="photo" style="background:linear-gradient(160deg,#c9cbc9,#eeeeec 50%,#4f6a48)" role="img" aria-label="Bathroom with freestanding tub and green plant wall"></div><span class="date">Dana 01.03.2021</span><span class="title">Home Remodeling Made Easier with Simple Tips</span></div>
  <div class="article" style="left:773px"><div class="photo" style="background:linear-gradient(160deg,#d6d4d2,#f2f1ef 55%,#a6a4a0)" role="img" aria-label="White bathroom vanity with round sinks"></div><span class="date">Dana 01.03.2021</span><span class="title">Handyman vs. Contractor – Who Should You Call?</span></div>
  <div class="btn-red" style="left:466px;top:3742px;width:268px;height:64px;font-size:22px">Read Our Blog</div>

  <!-- faq -->
  <h2 class="section-title" style="top:3882px">Frequently Asked Questions</h2>
  <div class="faq"><div>How much does a basement finish cost ?<span class="p">+</span></div><div>How long will it take?<span class="p">+</span></div><div>Do you pull permits?<span class="p">+</span></div><div>Are you licensed and insured ?<span class="p">+</span></div></div>

  <!-- other questions -->
  <div class="navy-band" style="top:4164px;height:126px"></div>
  <p class="abs center" style="top:4186px;font-size:19px;font-weight:600;color:#fff">Other Questions?</p>
  <p class="abs center" style="top:4226px;font-size:14px;color:#fff">Contact us at 555-204-7318 &nbsp; or Reach out to our
    <svg width="20" height="16" viewBox="0 0 20 16" style="vertical-align:-3px"><path d="M10 1C5 1 1 4 1 7.5c0 2 1.2 3.7 3 4.8L3 15l4-2c1 .3 2 .4 3 .4 5 0 9-3 9-6.4S15 1 10 1z" fill="#fff"/></svg> Support Team</p>

  <!-- footer -->
  <footer class="footer"></footer>
  <div class="brand" style="left:137px;top:4332px;font-size:24px"><span class="mark" style="width:22px;height:22px"></span>PLUMVANTA</div>
  <div class="social"><span style="background:#2f4f8f"></span><span style="background:#3a9be8"></span><span style="background:#d93025"></span><span style="background:#3f6f98"></span></div>
  <div class="foot-col" style="left:508px;top:4323px"><h5>Services</h5><ul><li>Basement Finishing</li><li>Bathroom Remodeling</li><li>Handyman</li><li>Kitchen Remodeling</li><li>Window Replacement</li><li>Whole Home Remodeling</li></ul></div>
  <div class="foot-col" style="left:820px;top:4314px"><h5>Service Areas</h5><ul><li>Ankeny, IA</li><li>Clive, IA</li><li>Des Moines, IA</li><li>Johnston, IA</li><li>Urbandale, IA</li><li>Waukee, IA</li><li>West Des Moines, IA</li><li>View All</li></ul></div>

  <div class="bottom"></div>
  <p class="abs" style="left:113px;top:4665px;font-size:8.5px;color:var(--ink)">Copyright ©2021 Plumvanta All Rights Reserved</p>
  <div class="abs" style="left:953px;top:4656px;display:flex;align-items:center;gap:12px;font-size:13px;color:var(--ink)">
    <svg width="32" height="32" viewBox="0 0 32 32"><circle cx="16" cy="16" r="15" fill="#1f2a3c"/><path d="M16 24V9M9 15l7-7 7 7" fill="none" stroke="#fff" stroke-width="3"/></svg>Back to top</div>

</div>
</body>
</html>
```